CATALOG COVER

CEDARLINE METAL & EDGE

THE FRONT COVER WILL CONSIST OF THE LOGO & THE BUILDERS CHOICE IN STEEL ROOFING & SIDING, THE FACTORY DIRECT SOURCE. (SAME FONT AS ON THE WEB SITE), PHONE NUMBER WEB SITE AND A STEEL BUILDING. THE BACK OF THE FRONT COVER NEEDS TO HAVE STEEL BUILDING PICTURES, SAME WITH THE INSIDE BACK COVER. AND THE LAST COVER PAGE NEEDS TO CONSIST OF THE LOGO, ADDRESS PICTURES OF BUILDING WEB SITE PHONE NUMBER (23 DIFFERENT COLORS, RESIDENTIAL, COMMERCIAL, AGRICULTURE, CONFINEMENTS, FAST, FRIENDLY QUALITY SERVICE) AND MORE.

WE HAVE LOTS OF PICTURES OF BUILDINGS ON THE WEBSITE THAT YOU CAN USE.
NO NAMES OF EMPLOYEES
ALSO I WANT THE LOGO TO BE ON TOP OF THE FRONT COVER.
PLEASE USE THE SAME FONT FOR FACTORY DIRECT SOURCE AS ON THE WEB SITE

WE MANUFACTURE BUILDINGS AND BUILDING COMPONENTS. EVERYTHING YOU NEED TO DESIGN THIS COVER WILL BE ON WWW.CEDARLINEMETALANDEDGE.EXAMPLE
You will design 4 panels which will be our outside and inside catalog cover.
So it will print both sides of a 11'' x 17'' paper and will be folded and stapled as the cover of the catalog.
please keep in mind we do not have FULL BLEED CAPABILITY.
therefore, images and print must not look like scrapbook.
We have been producing our own catalog for over two years but we desire a professional image. unfortunately we do not have full bleed capability and this has made our attempts look like a scrape book... pasting images and pictures that have borders. please note current catalog available on website.
inside front cover will not have table of contents so it will be "timeless" and not effect out many updates. same with all four panels.
WE ARE LOOKING FOR A PROFESSIONAL COVER
THANKS
Please call with question marty 555-014-2287
Updates

We cannot do FULL BLEED.  If you do not understand please find out what this means.

Also, I have just uploaded quite a bit of material, images to get ideas from.  

Reason: We have made some significant head way on the latest designs. We have posted many attachments since we started We have had excellent two-way feedback from two designers. Hoping we make a "Break Through" to take us to the next level !! Please look at the last four submissions to see our direction. Only one designer captured a way to provide a "fade" to our white cover paper.

can all designers see 3301645 ??

Target Market(s)

CONSTRUCTION COMPANIES AND FARMERS.

Industry/Entity Type

Agriculture

Font styles to use
Serif
Sans Serif

Colors
0555a3
ec2027
ffffff

Requirements
Must have
• PICTURES OF STEEL BUILDINGS AND CONSTRUCTION MATERIAL.
Use image Our Truck with Forklift on back cover, see word doc uploaded
Use images of buildings on inside front cover, see word doc uploaded
Nice to have
• USE THE EXISTING LOGO THAT'S ON FILE.
Use Dark Rich Blues and Reds that Match our Logo
Should not have
• NAMES OF EMPLOYEES OR EMAILS
TABLE OF CONTENTS

```html
<!DOCTYPE html>
<html lang="en">
<head>
<meta charset="utf-8">
<title>Cedarline Metal &amp; Edge – Catalog Cover</title>
<link rel="stylesheet" href="https://fonts.googleapis.com/css2?family=Arimo&family=Oswald:wght@600&family=PT+Sans&family=Roboto+Slab:wght@500;800&display=swap">
<style>
  :root{
    --brand-blue:#0555a3;
    --brand-red:#ec2027;
    --deep-red:#b3232a;
    --paper:#ffffff;
    --spine:#9fb3cc;
  }
  html,body{margin:0;padding:0;width:1200px;height:796px;overflow:hidden;background:var(--paper);}
  .cover{position:relative;width:1200px;height:796px;background:var(--paper);font-family:"Arimo",Arial,sans-serif;}
  .cover-art{position:absolute;inset:0;width:1200px;height:796px;}
  .headline{position:absolute;left:646px;top:196px;color:var(--paper);margin:0;font-weight:400;}
  .headline span{display:block;}
  .headline .h-the,.headline .h-choice{font-family:"PT Sans",sans-serif;font-size:56px;line-height:1;}
  .headline .h-builders{font-family:"Roboto Slab",serif;font-weight:800;font-size:58px;line-height:1;margin:22px 0 18px;text-shadow:2px 3px 2px rgba(0,0,0,.35);}
  .brand{position:absolute;display:flex;align-items:center;gap:8px;color:var(--brand-blue);font-family:"Oswald",sans-serif;font-weight:600;text-transform:uppercase;line-height:1.05;}
  .brand-mark{width:12px;height:12px;background:var(--brand-red);flex:none;}
  .brand-front{left:948px;top:132px;font-size:22px;}
  .brand-back{left:46px;top:528px;font-size:17px;}
  .contact{position:absolute;left:43px;top:614px;width:300px;}
  .contact h2{margin:0;font-family:"Roboto Slab",serif;font-weight:500;font-size:26px;color:var(--deep-red);padding-bottom:6px;border-bottom:1.5px solid var(--brand-blue);width:156px;}
  .contact ul{list-style:none;margin:10px 0 0;padding:0;color:var(--brand-blue);font-size:14px;}
  .contact li{display:flex;align-items:flex-start;gap:7px;margin-bottom:7px;line-height:17px;}
  .contact svg{flex:none;margin-top:2px;}
  .tagline{position:absolute;left:868px;top:708px;width:332px;height:58px;}
  .tagline-bg{position:absolute;inset:0;}
  .tagline p{position:absolute;right:18px;top:12px;margin:0;font-family:"PT Sans",sans-serif;font-size:27px;color:var(--brand-red);}
</style>
</head>
<body>
<main class="cover">
  <svg class="cover-art" viewBox="0 0 1200 796" aria-hidden="false">
    <defs>
      <linearGradient id="metalRoof" x1="0" y1="0" x2="1" y2="1">
        <stop offset="0" stop-color="#9aa3ad"/>
        <stop offset=".45" stop-color="#e9ebee"/>
        <stop offset="1" stop-color="#8a939c"/>
      </linearGradient>
      <linearGradient id="brickHouse" x1="0" y1="0" x2="0" y2="1">
        <stop offset="0" stop-color="#a9c6e4"/>
        <stop offset=".35" stop-color="#4a3a34"/>
        <stop offset=".6" stop-color="#d8d0bf"/>
        <stop offset="1" stop-color="#b49c7a"/>
      </linearGradient>
    </defs>

    <!-- spine -->
    <line class="spine" x1="600" y1="0" x2="600" y2="796" stroke="var(--spine)" stroke-width="1"/>

    <!-- photo: grey standing-seam steel roofs over white house -->
    <polygon class="photo photo-roof" role="img" aria-label="Photo of a white house with grey standing-seam steel roofs under a cloudy sky"
      points="0,0 557,0 208,298 93,404 0,318" fill="url(#metalRoof)"/>
    <polyline class="red-chevron" points="0,326 93,420 214,306" fill="none" stroke="var(--brand-red)" stroke-width="7"/>

    <!-- central blue diamond -->
    <polygon class="blue-diamond" points="557,0 670,0 996,311 662,640 557,640 208,298" fill="var(--brand-blue)"/>
    <line class="red-rule" x1="212" y1="316" x2="546" y2="640" stroke="var(--brand-red)" stroke-width="3"/>
    <line class="red-rule" x1="684" y1="0" x2="1008" y2="300" stroke="var(--brand-red)" stroke-width="4"/>

    <!-- photo: two-storey house with dark steel tile roof -->
    <polygon class="photo photo-house" role="img" aria-label="Photo of a two-storey brick and siding house with a dark steel tile roof"
      points="600,640 662,640 1004,318 1108,426 1200,334 1200,796 600,796" fill="url(#brickHouse)"/>
    <line class="red-rule" x1="668" y1="644" x2="1004" y2="322" stroke="var(--brand-red)" stroke-width="5"/>
    <polyline class="red-chevron" points="1008,306 1108,412 1200,318" fill="none" stroke="var(--brand-red)" stroke-width="8"/>
  </svg>

  <h1 class="headline">
    <span class="h-the">The</span>
    <span class="h-builders">Builders</span>
    <span class="h-choice">Choice</span>
  </h1>

  <div class="brand brand-front"><span class="brand-mark"></span><span>Cedarline<br>Metal &amp; Edge</span></div>
  <div class="brand brand-back"><span class="brand-mark"></span><span>Cedarline<br>Metal &amp; Edge</span></div>

  <section class="contact">
    <h2>Contact Us</h2>
    <ul>
      <li>
        <svg width="10" height="13" viewBox="0 0 10 13"><path d="M5 0a5 5 0 0 1 5 5c0 3-5 8-5 8S0 8 0 5a5 5 0 0 1 5-5z" fill="var(--brand-red)"/><circle cx="5" cy="5" r="1.8" fill="#fff"/></svg>
        <span>1420 Prairie Line Rd Harlow<br>SD 57000</span>
      </li>
      <li>
        <svg width="12" height="12" viewBox="0 0 12 12"><circle cx="6" cy="6" r="5.3" fill="none" stroke="var(--brand-red)" stroke-width="1.2"/><path d="M4 3.2l1.2 1.4-.7.9c.4.8 1 1.4 1.8 1.8l.9-.7 1.4 1.2-.8 1c-2.3-.3-4.2-2.2-4.6-4.6z" fill="var(--brand-red)"/></svg>
        <span>555-014-3390</span>
      </li>
      <li>
        <svg width="14" height="12" viewBox="0 0 14 12"><rect x="3" y="0" width="8" height="4" fill="var(--brand-red)"/><rect x="0" y="4" width="14" height="5" rx="1" fill="var(--brand-red)"/><rect x="3" y="7" width="8" height="5" fill="#fff" stroke="var(--brand-red)"/></svg>
        <span>555-014-7715</span>
      </li>
      <li>
        <svg width="11" height="11" viewBox="0 0 12 12"><circle cx="6" cy="6" r="5.3" fill="none" stroke="var(--brand-red)" stroke-width="1.3"/><path d="M1 6h10M6 1v10M6 1c-2.5 3-2.5 7 0 10M6 1c2.5 3 2.5 7 0 10" fill="none" stroke="var(--brand-red)" stroke-width="1"/></svg>
        <span>www.cedarlinemetalandedge.example</span>
      </li>
    </ul>
  </section>

  <div class="tagline">
    <svg class="tagline-bg" viewBox="0 0 332 58" preserveAspectRatio="none"><polygon points="22,0 332,0 332,58 0,58" fill="#f4f4f4" opacity=".92"/></svg>
    <p>Steel Roofing &amp; Siding</p>
  </div>
</main>
</body>
</html>
```